Business Value Optimisation Consultancy Needs a Web Design

Velor Quintess is a business consultancy in Australia, which assists SMEs (small; to medium sized businesses) to grow revenue signicantly, put in professional operaations, and become worth a lot more as a sale-able business.

It is in need of new website design (you can see the current "old" site here at www.velorquintess.net - please note all content has changed for the new site - please see content file attached).

An example of a site we like is www.bluekestrelhub.com.au because:

a. it is crisp and clear, and quickly conveys what the offering is all about.
b. it offers a report download with email sign up.
c. it is easy and simple to navigate

We don't want an exact copy of this site, but this site is given as an example of the type of clear design we like.

Another example is:

Also, please see the attached powerpoint presentation - please note the style used in it - we would like the website to be close to the powerpoint style but it does not have to be exactly the same.

2. please see attached files with:

a. content for all pages - note the content makes reference to some videos
b. a list of all available videos, as hosted on vimeo
c. blog posts written to date
d. a powerpoint presentation used by Velor Quintess - please keep the site design in line with the style used in this powerpoint presentation.

Designs to be supplied as PSD files.

Thank you!

Target Market(s)

Small to Medium Sized Professional Service Businesses
Technology Start Ups
Medium Businesses Approaching Small Corporate Size

Industry/Entity Type

Business Consultant

Number of Pages Required

3 page

Font styles to use
Sans Serif

Requirements
Must have
• Home Page
• Inner Page
• Blog

```html
<!DOCTYPE html>
<html lang="en">
<head>
<meta charset="utf-8">
<title>Velor Quintess – What We Do</title>
<link rel="stylesheet" href="https://fonts.googleapis.com/css2?family=Open+Sans:wght@400;600;700&family=Roboto+Slab:wght@400;700&display=swap">
<style>
:root{
  --navy:#1c2935;
  --teal:#2aa7d9;
  --band:#cfe8f4;
  --grey:#ededed;
  --grey-line:#d6d6d6;
  --ink:#333a40;
  --muted:#7b8288;
  --white:#ffffff;
  --footer:#2a2c2e;
  --footer-bar:#1f2022;
  --video-a:#2c5d80;
  --video-b:#7fa9c4;
}
*{box-sizing:border-box;margin:0;padding:0}
html,body{width:730px;height:1200px;overflow:hidden}
body{font-family:"Open Sans",sans-serif;color:var(--ink);background:var(--white);font-size:7px;line-height:1.5}
.slab{font-family:"Roboto Slab",serif}

/* header */
.site-header{height:100px;background:var(--navy);position:relative}
.main-nav{display:flex;justify-content:space-between;padding:0 30px;height:20px}
.main-nav ul{display:flex;list-style:none}
.main-nav li{color:var(--white);font-size:6.5px;font-weight:600;letter-spacing:.4px;padding:0 11px;line-height:20px;text-transform:uppercase}
.main-nav li.active{background:var(--teal)}
.brand{position:absolute;left:50%;top:50px;transform:translateX(-50%);text-align:center;color:var(--white);white-space:nowrap}
.brand-name{font-size:15px;font-weight:700;letter-spacing:1.5px}
.brand-tag{font-size:6px;color:var(--band);margin-top:1px}

/* title band */
.page-title{height:56px;background:var(--band);padding:0 55px;display:flex;align-items:center}
.page-title h1{font-weight:400;font-size:24px;color:var(--navy)}

/* intro */
.intro{display:flex;justify-content:space-between;padding:30px 55px 0;height:205px}
.intro-text{width:330px}
.intro-text h2{font-size:14px;font-weight:700;color:var(--navy);margin-bottom:8px}
.intro-text p{margin-bottom:7px;color:var(--muted)}
.intro-video{width:250px}
.video-caption{font-size:7px;font-weight:600;color:var(--navy);margin-bottom:4px}
.video-frame{position:relative;background:linear-gradient(135deg,var(--video-a),var(--video-b));height:110px}
.play{position:absolute;left:50%;top:50%;transform:translate(-50%,-50%)}

/* steps */
.release{background:var(--grey);height:270px;padding:46px 55px 0;text-align:center;border-top:1px solid var(--grey-line)}
.release h2{font-size:14px;font-weight:700;color:var(--navy);margin-bottom:8px}
.release p{color:var(--muted);width:470px;margin:0 auto 14px}
.download-btn{display:inline-block;border:1px solid var(--grey-line);background:var(--white);color:var(--navy);font-size:8px;font-weight:600;padding:7px 18px;margin-bottom:16px}
.steps{display:flex;gap:8px;justify-content:center}
.step{width:148px;background:var(--white);border-top:3px solid var(--teal);padding:7px 8px 9px;text-align:left}
.step-no{color:var(--teal);font-size:7px;text-align:center;display:block;margin-bottom:2px}
.step-name{font-size:9.5px;color:var(--navy)}

/* videos */
.videos{display:flex;justify-content:center;gap:22px;padding:22px 0 0;height:160px}
.video-card{width:178px;text-align:center}
.video-card h3{font-size:8.5px;font-weight:600;color:var(--navy);margin-bottom:6px}
.video-card .video-frame{height:110px}

/* talk */
.talk{text-align:center;height:110px;padding-top:26px}
.talk h2{font-size:15px;font-weight:700;color:var(--navy);margin-bottom:6px}
.talk p{color:var(--teal);font-size:8.5px;font-weight:600;line-height:1.6}

/* contact */
.contact{background:var(--grey);height:120px;text-align:center;padding-top:20px}
.contact h2{font-size:16px;font-weight:400;color:var(--navy);margin-bottom:6px}
.contact p{color:var(--muted);margin-bottom:10px}
.contact-form{display:flex;gap:6px;justify-content:center}
.field{width:100px;height:14px;background:var(--white);border:1px solid var(--grey-line);font-size:6px;color:var(--muted);text-align:left;padding:2px 5px}
.field.wide{width:180px}
.submit{background:var(--teal);color:var(--white);font-size:6px;font-weight:700;padding:2px 10px;height:14px}

/* footer */
.site-footer{background:var(--footer);height:155px;padding:20px 55px 0;display:flex;gap:38px;color:#b9bcbf}
.footer-col h4{font-size:6.5px;color:var(--white);font-weight:700;margin-bottom:6px;text-transform:uppercase}
.footer-col ul{list-style:none;font-size:6px;line-height:1.9}
.footer-links{display:flex;gap:22px}
.newsletter .field{width:110px;margin-bottom:5px}
.socials{display:flex;gap:4px}
.socials span{width:12px;height:12px;border-radius:50%;background:var(--teal)}
.footer-bar{background:var(--footer-bar);height:24px;padding:0 55px;display:flex;align-items:center;justify-content:space-between;color:#8c9093;font-size:6px}
.footer-bar .dots{display:flex;gap:4px}
.footer-bar .dots span{width:9px;height:9px;border-radius:50%;border:1px solid #8c9093}
</style>
</head>
<body>

<header class="site-header">
  <nav class="main-nav">
    <ul><li>Home</li><li>Who We Are</li><li class="active">What We Do</li><li>Who We Work With</li></ul>
    <ul><li>Resources</li><li>Events</li><li>Blog</li><li>Contact Us</li></ul>
  </nav>
  <div class="brand">
    <div class="brand-name">VELOR QUINTESS</div>
    <div class="brand-tag">Growth Advisory for SMEs</div>
  </div>
</header>

<section class="page-title"><h1>What We Do</h1></section>

<section class="intro">
  <div class="intro-text">
    <h2 class="slab">Are you a Diamond in the Rough?</h2>
    <p>Diamond cutting is a lengthy process requiring knowledge, skill and precise planning to turn the stone's imperfections, polishing to reveal its best qualities, and ultimately create a gem worth many times over its original value.</p>
    <p>Same goes for a business.</p>
    <p>Of course, it all starts with the original stone: does it have the inherent potential to be something great?</p>
  </div>
  <div class="intro-video">
    <div class="video-caption">VIDEO: A Barrier to Growth? What Do YOU See?</div>
    <div class="video-frame" role="img" aria-label="Video still introducing the business growth barrier">
      <svg class="play" width="26" height="26" viewBox="0 0 26 26"><circle cx="13" cy="13" r="13" fill="#2aa7d9"/><path d="M10 8 L19 13 L10 18 Z" fill="#fff"/></svg>
    </div>
  </div>
</section>

<section class="release">
  <h2 class="slab">Release Potential, Optimise Value, in 3-5 years. Really</h2>
  <p>Our way of thinking at Velor Quintess is unique. Our 4-Step Optimisation Solution moves your business from a modest daily successful entrepreneurial operation – a "diamond in the rough" – to a fully realised, "corporate" sale-worth every latest move. Within 3 to 5 years.</p>
  <div class="download-btn">Download a copy of our 4-Step Optimisation Solution to understand how and why it works.</div>
  <div class="steps">
    <div class="step"><span class="step-no">Step 1</span><div class="step-name">Identify and diagnose</div></div>
    <div class="step"><span class="step-no">Step 2</span><div class="step-name">Engineer for performance</div></div>
    <div class="step"><span class="step-no">Step 3</span><div class="step-name">Equip for success</div></div>
    <div class="step"><span class="step-no">Step 4</span><div class="step-name">Reap the rewards</div></div>
  </div>
</section>

<section class="videos">
  <div class="video-card">
    <h3>More than just Consulting</h3>
    <div class="video-frame" role="img" aria-label="Video still about consulting services">
      <svg class="play" width="24" height="24" viewBox="0 0 26 26"><circle cx="13" cy="13" r="13" fill="#2aa7d9"/><path d="M10 8 L19 13 L10 18 Z" fill="#fff"/></svg>
    </div>
  </div>
  <div class="video-card">
    <h3>Why You Need A Sellable Business</h3>
    <div class="video-frame" role="img" aria-label="Video still about building a sellable business">
      <svg class="play" width="24" height="24" viewBox="0 0 26 26"><circle cx="13" cy="13" r="13" fill="#2aa7d9"/><path d="M10 8 L19 13 L10 18 Z" fill="#fff"/></svg>
    </div>
  </div>
  <div class="video-card">
    <h3>The Value of Perspective</h3>
    <div class="video-frame" role="img" aria-label="Video still about the value of perspective">
      <svg class="play" width="24" height="24" viewBox="0 0 26 26"><circle cx="13" cy="13" r="13" fill="#2aa7d9"/><path d="M10 8 L19 13 L10 18 Z" fill="#fff"/></svg>
    </div>
  </div>
</section>

<section class="talk">
  <h2 class="slab">Let's talk business.</h2>
  <p>Contact us at +61 3 9555 0148 or skype: velorquintess<br>Email: hello@velorquintess.net</p>
</section>

<section class="contact">
  <h2>Contact Us</h2>
  <p>Your time is precious. Tell us a little about your business and we will reply soon.<br>We'd love to hear where your plans are heading and how we can help you get there.</p>
  <div class="contact-form">
    <div class="field">Name</div>
    <div class="field">Email</div>
    <div class="field">Phone</div>
    <div class="field wide">Message</div>
    <div class="submit">SUBMIT</div>
  </div>
</section>

<footer class="site-footer">
  <div class="footer-col">
    <h4>Quick Links</h4>
    <div class="footer-links">
      <ul><li>Home</li><li>Who we are</li><li>What we do</li><li>Who We Work With</li></ul>
      <ul><li>Resources</li><li>Events</li><li>Blog</li><li>Contact Us</li></ul>
    </div>
  </div>
  <div class="footer-col">
    <h4>Contact Us</h4>
    <ul><li>Tel: +61 3 9555 0148</li><li>Email: hello@velorquintess.net</li><li>Skype: velorquintess</li></ul>
  </div>
  <div class="footer-col">
    <h4>News</h4>
    <div class="footer-links">
      <ul><li>Value in growth</li><li>Team planning</li><li>Exit readiness</li><li>Latest event</li></ul>
      <ul><li>Scaling systems</li><li>Client stories</li><li>Profit drivers</li><li>Annual review</li></ul>
    </div>
  </div>
  <div class="footer-col newsletter">
    <h4>Newsletter</h4>
    <div class="field">Your email</div>
    <div class="socials"><span></span><span></span><span></span><span></span></div>
  </div>
</footer>
<div class="footer-bar">
  <span>Copyright © 2015 Velor Quintess. All rights reserved.</span>
  <div class="dots"><span></span><span></span></div>
</div>

</body>
</html>
```